Bulldog themed background for Real Estate Purchase Letter

I need a phantom background or watermark on a standard 8 1/2" x 11" paper. I am going to put a letter over the background. I want a bulldog theme that is cute, funny and original. This letter is for a real estate project and we want to capture the person sub-consciously . Attached is my personal dogs. If you want to use them you can but not required. I have attached the letter that I am trying to emulate. I want bulldogs not horses.

Target Market(s)

45 years old and higher

Industry/Entity Type

Real Estate

Font styles to use
Serif
Sans Serif

Colors

Designer to choose colors to be used in the design.

Requirements
Must have
• fun, happiness, reassuring,
Should not have
• violence, negativity, unhappy

```html
<!DOCTYPE html>
<html lang="en">
<head>
<meta charset="utf-8">
<title>Maple Row Homes – Letterhead</title>
<link href="https://fonts.googleapis.com/css2?family=Source+Sans+3:wght@400;600;700&display=swap" rel="stylesheet">
<style>
  :root {
    --backdrop: #237bc8;
    --paper: #ffffff;
    --ink-heading: #777777;
    --ink-body: #4f4f4f;
    --ink-footer: #3c3c3c;
    --mark: #767676;
    --watermark-light: #f4f4f4;
    --watermark-mid: #dcdcdc;
  }
  * { box-sizing: border-box; margin: 0; padding: 0; }
  html, body {
    width: 1200px;
    height: 1118px;
    overflow: hidden;
    background: var(--backdrop);
    font-family: "Source Sans 3", "Helvetica Neue", Arial, sans-serif;
  }
  .letterhead {
    position: absolute;
    left: 284px;
    top: 148px;
    width: 680px;
    height: 882px;
    background: var(--paper);
    overflow: hidden;
  }
  .letterhead__watermark {
    position: absolute;
    left: 112px;
    top: 305px;
    width: 412px;
    height: 600px;
    border-radius: 46% 46% 0 0 / 34% 34% 0 0;
    background: radial-gradient(ellipse at 50% 45%, var(--watermark-mid) 0%, var(--watermark-light) 55%, rgba(255,255,255,0) 80%);
    opacity: 0.75;
  }
  .brand {
    position: absolute;
    left: 148px;
    top: 110px;
    display: flex;
    align-items: center;
    gap: 10px;
    font-size: 20px;
    font-weight: 700;
    color: var(--mark);
  }
  .brand__square {
    width: 14px;
    height: 14px;
    background: var(--mark);
  }
  .letter {
    position: absolute;
    left: 152px;
    top: 272px;
    width: 370px;
  }
  .letter__headline {
    font-size: 17px;
    font-weight: 700;
    color: var(--ink-heading);
    margin-left: -1px;
    margin-bottom: 30px;
  }
  .letter__para {
    font-size: 9.6px;
    line-height: 16.1px;
    color: var(--ink-body);
    text-align: justify;
    hyphens: auto;
    margin-bottom: 14px;
  }
  .contact {
    position: absolute;
    left: 152px;
    top: 728px;
    font-size: 9.6px;
    color: var(--ink-footer);
  }
  .contact__row {
    display: flex;
    gap: 0;
    font-weight: 700;
  }
  .contact__phone { width: 130px; }
  .contact__address {
    margin-top: 13px;
    line-height: 16px;
    font-weight: 400;
  }
</style>
</head>
<body>
  <main class="letterhead">
    <div class="letterhead__watermark" role="img" aria-label="Faint black and white watermark of a smiling bulldog sitting behind the letter text"></div>

    <div class="brand">
      <span class="brand__square"></span>
      <span class="brand__name">Maple Row Homes</span>
    </div>

    <article class="letter">
      <h1 class="letter__headline">Sample Headline Here</h1>
      <p class="letter__para">Lorem Ipsum is simply dummy text of the printing and typesetting industry. Lorem Ipsum has been the industry's standard dummy text ever since the 1500s, when an unknown printer took a galley of type and scrambled it to make a type specimen book. It has survived not only five centuries, but also the leap into electronic typesetting, remaining essentially unchanged. It was popularised in the 1960s with the release of Letraset sheets containing Lorem Ipsum passages, and more recently with desktop publishing software like Aldus PageMaker including versions of Lorem Ipsum.</p>
      <p class="letter__para">Lorem Ipsum is simply dummy text of the printing and typesetting industry. Lorem Ipsum has been the industry's standard dummy text ever since the 1500s, when an unknown printer took a galley of type and scrambled it to make a type specimen book. It</p>
      <p class="letter__para">Lorem Ipsum is simply dummy text of the printing and typesetting industry. Lorem Ipsum has been the industry's standard dummy text ever since the 1500s, when an unknown printer took a galley of type and scrambled it to make a type specimen book. It has survived not only five centuries, but also the leap into electronic typesetting, remaining essentially unchanged. It was popularised in the 1960s with the release of Letraset sheets containing Lorem Ipsum passages, and more recently with desktop publishing software like Aldus PageMaker including versions of Lorem Ipsum.</p>
    </article>

    <footer class="contact">
      <div class="contact__row">
        <span class="contact__phone">(555) 214-3870</span>
        <span class="contact__email">hello@maplerowhomes.net</span>
      </div>
      <address class="contact__address" style="font-style:normal">
        412 North Birchwood Lane<br>
        Cedar Falls, IA 50613
      </address>
    </footer>
  </main>
</body>
</html>
```